Teachers workshop flyer

I need a flyer to inform schools of a workshop for teachers that empowers the teacher to help traumatised and disadvantaged students to engage in successful learning.

I am a teacher and educator and my info for the flyer is attached.

Target Market(s)

Principals and vice-principals who have stressed staff and students and they want things to be better in the school!

Industry/Entity Type

Teacher

```html
<!DOCTYPE html>
<html lang="en">
<head>
<meta charset="utf-8">
<title>Brain-Based Strategies for Student Success</title>
<link href="https://fonts.googleapis.com/css2?family=Andika:wght@400;700&family=Arvo:ital,wght@0,400;1,400&display=swap" rel="stylesheet">
<style>
  :root {
    --page-bg: #ffffff;
    --frame: #c3bf9c;
    --green-top: #36e38e;
    --green-bottom: #40f24b;
    --title-green: #3fdc86;
    --ink-blue: #2f7ee0;
    --white: #ffffff;
    --box-border: #2fc88a;
  }
  * { margin: 0; padding: 0; box-sizing: border-box; }
  html, body { width: 1200px; height: 1000px; overflow: hidden; background: var(--page-bg); }
  body { font-family: "Andika", "Trebuchet MS", sans-serif; }

  .canvas { position: relative; width: 1200px; height: 1000px; }
  .flyer-frame { position: absolute; left: 207px; top: 0; width: 786px; height: 1000px; background: var(--frame); }
  .flyer {
    position: absolute; left: 235px; top: 20px; width: 730px; height: 960px;
    background: linear-gradient(180deg, var(--green-top) 0%, var(--green-bottom) 100%);
  }

  .header-art {
    position: absolute; left: 272px; top: 30px; width: 132px; height: 126px;
    background: radial-gradient(circle at 50% 50%, #3d8f4c 0%, #6cc873 45%, rgba(54,227,142,0) 78%);
  }

  .title-badge { position: absolute; left: 356px; top: 48px; width: 490px; height: 186px; }
  .title-badge svg { position: absolute; inset: 0; }
  .title-text { position: absolute; left: 0; top: 34px; width: 100%; text-align: center; }
  .title-main {
    font-family: "Arvo", Georgia, serif; font-style: italic; font-weight: 400;
    font-size: 44px; line-height: 42px; color: var(--title-green);
    letter-spacing: 1px; padding-left: 40px;
  }
  .title-sub {
    font-family: "Arvo", Georgia, serif; font-size: 20px; letter-spacing: 2px;
    color: var(--ink-blue); margin-top: 6px; padding-left: 30px;
  }

  .intro {
    position: absolute; left: 263px; top: 258px; width: 690px;
    color: var(--white); font-size: 19px; line-height: 24px; letter-spacing: 0.5px;
    white-space: nowrap;
  }
  .intro .indent { padding-left: 60px; }
  .intro strong { font-weight: 700; }

  .section-label { position: absolute; color: var(--white); font-weight: 700; font-size: 14px; letter-spacing: 0.5px; }
  .label-presenter { left: 490px; top: 408px; }
  .label-feedback { left: 738px; top: 468px; }

  .info-card {
    position: absolute; background: var(--white);
    border: 2px solid var(--box-border); border-radius: 12px;
    box-shadow: 4px 5px 8px rgba(0,0,0,0.25);
    color: var(--ink-blue); font-size: 14px; line-height: 21px;
    white-space: nowrap; overflow: hidden;
  }
  .card-approach { left: 263px; top: 500px; width: 251px; height: 326px; padding: 8px 0 0 16px; }
  .card-presenter { left: 473px; top: 432px; width: 250px; height: 326px; padding: 4px 0 0 16px; z-index: 2; }
  .card-feedback { left: 688px; top: 500px; width: 251px; height: 326px; padding: 11px 0 0 49px; }

  .presenter-name { font-size: 26px; line-height: 34px; }
  .moments { font-weight: 700; font-size: 13px; line-height: 18.5px; margin-top: 2px; }
  .moments ul { list-style: none; }
  .moments li { position: relative; padding-left: 13px; }
  .moments li::before { content: "•"; position: absolute; left: 0; }

  .contact {
    position: absolute; left: 276px; top: 862px; width: 680px;
    color: var(--white); font-weight: 700; font-size: 20px; line-height: 25px; letter-spacing: 0.3px;
  }
  .return-arrow { position: absolute; left: 886px; top: 896px; width: 66px; height: 62px; }
</style>
</head>
<body>
<div class="canvas">
  <div class="flyer-frame"></div>
  <main class="flyer"></main>

  <div class="header-art" role="img" aria-label="Illustration of a sheet of paper with a pen on a halftone dot background"></div>

  <header class="title-badge">
    <svg width="490" height="186" viewBox="0 0 490 186" aria-hidden="true">
      <defs>
        <filter id="badgeShadow" x="-10%" y="-10%" width="130%" height="140%">
          <feDropShadow dx="5" dy="7" stdDeviation="5" flood-color="#000" flood-opacity="0.3"/>
        </filter>
      </defs>
      <ellipse cx="243" cy="90" rx="237" ry="88" fill="#ffffff" filter="url(#badgeShadow)"/>
    </svg>
    <div class="title-text">
      <h1 class="title-main">BRAIN-BASED<br>STRATEGIES</h1>
      <p class="title-sub">FOR STUDENT SUCCESS</p>
    </div>
  </header>

  <p class="intro"><span class="indent">Contemporary teaching is a highly complex role as increasing</span><br>numbers of students attend school without the essential <strong>‘self-skills’</strong> to<br>be truly <strong>‘school-ready’</strong> and <strong>successful</strong>. Instead these students often<br>seek-out attention in ways that can disruptive in the classroom causing<br>stress and frustration for teachers.</p>

  <h2 class="section-label label-presenter">ABOUT THE PRESENTER:</h2>
  <h2 class="section-label label-feedback">TEACHER FEEDBACK:</h2>

  <section class="info-card card-approach">
    <p>Declan shows how and why<br>the most effective strat-<br>egies for these students<br>are guided by a sound<br>understanding of child-<br>development and brain-<br>development - especially<br>where trauma has left<br>lasting impacts. Teachers<br>can learn how to build<br>a student’s self-skills,<br>without the teacher<br>having to become a<br>therapist!</p>
  </section>

  <section class="info-card card-presenter">
    <p class="presenter-name">Declan Harrow</p>
    <p>is a Melbourne-based therapist<br>and educator with over twenty<br>years experience working with<br>adults and young people in the<br>area of trauma and recovery.<br>Declan’s seminars are engaging<br>and practical since teachers<br>need effective strategies that<br>will immediately translate into<br>classroom practice. Declan has<br>trained here and overseas in<br>the most effective behavior<br>change strategies.</p>
  </section>

  <section class="info-card card-feedback">
    <p class="quote">“Declan was such an engaging<br>and energetic presenter<br>whom I enjoyed immensely.<br>His presentation on the<br>brain and take away<br>strategies were so practical<br>and meaningful. It was an<br>invaluable session.”</p>
    <div class="moments">
      <p>&nbsp;“My Light-bulb moments:</p>
      <ul>
        <li>I need to CONNECT - not<br>correct - far more often.</li>
        <li>Seeing negative self-talk<br>for what it is.</li>
        <li>Using far more ‘diversions’<br>in the avoidance loop.”</li>
      </ul>
    </div>
  </section>

  <footer class="contact">
    <p>Call: 0400 123 456</p>
    <p>for more information or to book Declan to come to your school:</p>
    <p>www.declanharrow.com.au/studentsuccess</p>
  </footer>

  <svg class="return-arrow" viewBox="0 0 66 62" aria-hidden="true">
    <path d="M58 4 C66 22 58 44 30 46 L30 58 L4 38 L30 20 L30 32 C48 32 56 20 58 4 Z"
          fill="#3fe27a" stroke="#1f6e3a" stroke-width="2" stroke-linejoin="round"/>
  </svg>
</div>
</body>
</html>
```